Book cover design for my new Bankruptcy Law Book

Hi

I would like to get a unique and nice design for my new book titled: "Quiet Harbors and the Lantern Keeper's Final Season".

I like blue color. It will be in Arabic so I care the most about the design of the book cover and not the words on the cover as the printing company will handle the rest.

Much appreciated,

KAREEM HADDAWI

Colors
0692cd
33a6d7
86cae7
85abd2
3277b5
0255a3

Requirements
Must have
• Blue color
Nice to have
• pictures or shapes related to bankruptcy or insolvency

```html
<!DOCTYPE html>
<html lang="en">
<head>
<meta charset="utf-8">
<title>Quiet Harbors and the Lantern Keeper's Final Season — Cover</title>
<link rel="stylesheet" href="https://fonts.googleapis.com/css2?family=Amiri:wght@700&family=Cairo:wght@500;800&display=swap">
<style>
  :root {
    --sky-top: #3f7fc2;
    --sky-mid: #6fa3d3;
    --sky-low: #bcd3e6;
    --haze: #e4e4e0;
    --skyline: #8e9aa8;
    --sand-top: #c79c6a;
    --sand-bottom: #9b6f45;
    --trend-red: #c8323a;
    --ink-white: #ffffff;
  }
  html, body {
    margin: 0;
    padding: 0;
    width: 800px;
    height: 1200px;
    overflow: hidden;
    background: #ffffff;
  }
  .cover {
    position: relative;
    width: 800px;
    height: 1200px;
    overflow: hidden;
  }
  .cover-scene {
    position: absolute;
    inset: 0;
    background: linear-gradient(
      to bottom,
      var(--sky-top) 0%,
      var(--sky-mid) 35%,
      var(--sky-low) 58%,
      var(--haze) 66%,
      var(--skyline) 76%,
      var(--sand-top) 80%,
      var(--sand-bottom) 100%
    );
  }
  .trend-chart {
    position: absolute;
    left: 0;
    top: 0;
    width: 800px;
    height: 1200px;
  }
  .title-block {
    position: absolute;
    top: 40px;
    left: 0;
    width: 800px;
    text-align: center;
    color: var(--ink-white);
  }
  .title-main {
    margin: 0;
    font-family: "Amiri", serif;
    font-weight: 700;
    font-size: 112px;
    line-height: 1.15;
    letter-spacing: 1px;
  }
  .title-sub {
    margin: 18px 0 0;
    font-family: "Cairo", sans-serif;
    font-weight: 500;
    font-size: 36px;
    line-height: 1.2;
  }
  .author {
    position: absolute;
    bottom: 36px;
    left: 0;
    width: 800px;
    margin: 0;
    text-align: center;
    font-family: "Cairo", sans-serif;
    font-weight: 800;
    font-size: 62px;
    letter-spacing: 3px;
    color: var(--ink-white);
  }
</style>
</head>
<body>
  <main class="cover">
    <div class="cover-scene" role="img" aria-label="Photograph of a modern city skyline of glass towers under a blue sky, with desert sand in the foreground and banknotes curling across the sand"></div>

    <svg class="trend-chart" viewBox="0 0 800 1200" aria-hidden="true">
      <polyline points="-10,596 208,482 277,532 346,532 378,446 457,526 552,410 664,594"
                fill="none" stroke="var(--trend-red)" stroke-width="26"
                stroke-linejoin="miter" stroke-opacity="0.85"/>
      <polygon points="632,602 701,634 688,560" fill="var(--trend-red)" fill-opacity="0.85"/>
    </svg>

    <header class="title-block">
      <h1 class="title-main">Quiet Harbors</h1>
      <p class="title-sub">and the Lantern Keeper's Final Season</p>
    </header>

    <p class="author">KAREEM HADDAWI</p>
  </main>
</body>
</html>
```